Castora Hub Brochure

We are an online casting website for Talents & Crew in the entertainment industry, the site has 3 different user categories:

1. Creator : as in producer or some one casting for talents and posting crew jobs
2. Talent: actors, performers or extras building their profile to apply for an audition posted by creators
3. Crew: behind the camera professionals who can build their profile online and apply for the jobs posted by creators

A 4 page brochure accordion fold with main page including the company logo and small brief about us, the second page has the creator aspect and what it does, the third is the talent and what it does, the fourth is the crew, you can see the website to have an idea about each of these categories www.CastoraHub.com, please feel free to ask any questions at time, I'm attaching two files, the first is the company logo and the second is a design reference, good luck

Target Market(s)

Film Makers, Producers, Actors and Professional Crew in the Middle East and North Africa region

Industry/Entity Type

Entertainment

Requirements
Must have
• Company logo, pictures, using logo font
Nice to have
• Modern artistic look, cutting edge design, catchy
Should not have
• Basic or boring look

```html
<!DOCTYPE html>
<html lang="en">
<head>
<meta charset="UTF-8">
<title>Castora Hub – Talent &amp; Crew</title>
<link href="https://fonts.googleapis.com/css2?family=Montserrat:wght@400;600;700&display=swap" rel="stylesheet">
<style>
  :root{
    --sky:#1aa3e0;
    --navy:#1c2a5e;
    --stripe:#1f8fd6;
    --text:#5a5a5a;
    --muted:#a3a7ab;
    --icon:#9aa0a6;
    --paper:#ffffff;
    --paper-end:#e6e7ea;
  }
  *{margin:0;padding:0;box-sizing:border-box}
  html,body{width:1200px;height:855px;overflow:hidden;background:#fff}
  .spread{position:relative;width:1200px;height:855px;overflow:hidden;
    font-family:"Montserrat",Arial,sans-serif;color:var(--text);
    background:linear-gradient(#fff 0,#fff 520px,var(--paper-end) 855px)}
  .spread::after{content:"";position:absolute;left:10px;right:10px;top:0;bottom:12px;
    border:1px solid #e3e4e6;border-top:none;pointer-events:none}
  .photo{position:absolute;top:0;height:305px}
  .photo--stage{left:8px;width:590px;
    background:radial-gradient(circle at 45% 40%,#5b3a52 0,#2a1a2a 35%,#0c0a10 75%)}
  .photo--camera{left:598px;width:594px;
    background:radial-gradient(circle at 75% 30%,#c8a470 0,#7a5a36 35%,#2a2018 80%)}
  .header-curve{position:absolute;left:0;top:0}
  .badge{position:absolute;left:36px;top:222px;width:136px;height:136px;border-radius:50%;
    background:var(--navy);border:3px solid #fff;display:flex;align-items:center;justify-content:center;
    text-align:center;color:#fff;font-weight:600;font-size:21px;line-height:1.1}
  .panel{position:absolute;top:290px;width:536px;height:500px}
  .panel--talent{left:42px}
  .panel--crew{left:605px}
  .panel__title{font-size:60px;font-weight:700;color:var(--sky);text-align:right;line-height:66px;letter-spacing:-1px}
  .panel__intro{margin-top:6px;font-size:11.5px;line-height:15.2px;text-align:justify;letter-spacing:.15px}
  .features{position:absolute;left:0;top:0;width:536px;height:500px}
  .feature{position:absolute;width:256px;display:flex}
  .feature__icon{flex:none;width:46px;height:46px;border-radius:50%;background:var(--icon);
    display:flex;align-items:center;justify-content:center;margin-right:8px;margin-top:2px}
  .feature__title{font-size:13px;font-weight:700;color:var(--muted);line-height:14px}
  .feature__text{font-size:13.6px;line-height:15.4px;text-align:justify;color:#666}
  .c1{left:0}.c2{left:276px}
  .r1{top:232px}.r2{top:312px}.r3{top:394px}
  .c2.r3{top:398px}
</style>
</head>
<body>
<div class="spread">
  <div class="photo photo--stage" role="img" aria-label="Performer in a flowing gown on a lit theatre stage"></div>
  <div class="photo photo--camera" role="img" aria-label="Smiling camera operator behind a film camera on set"></div>

  <svg class="header-curve" width="1200" height="320" viewBox="0 0 1200 320" aria-hidden="true">
    <path d="M0,262 Q600,200 1200,270 L1200,280 Q600,212 0,272 Z" fill="var(--stripe)"/>
    <path d="M0,272 Q600,212 1200,280 L1200,298 Q600,232 0,290 Z" fill="var(--navy)"/>
    <path d="M0,290 Q600,232 1200,298 L1200,320 L0,320 Z" fill="#fff"/>
  </svg>

  <div class="badge">Castora<br>Hub</div>

  <svg width="0" height="0" style="position:absolute" aria-hidden="true">
    <defs>
      <g id="icon-sun" fill="#fff"><circle cx="12" cy="12" r="5"/><g stroke="#fff" stroke-width="2" stroke-linecap="round"><path d="M12 1v3M12 20v3M1 12h3M20 12h3M4.2 4.2l2.1 2.1M17.7 17.7l2.1 2.1M4.2 19.8l2.1-2.1M17.7 6.3l2.1-2.1"/></g></g>
      <g id="icon-basket" fill="none" stroke="#fff" stroke-width="2" stroke-linejoin="round"><path d="M3 10h18l-2 10H5z"/><path d="M7 10l4-6M17 10l-4-6M9 13v4M12 13v4M15 13v4"/></g>
      <g id="icon-chat" fill="#fff"><path d="M3 4h18v12H9l-5 4v-4H3z"/><path d="M7 8h10M7 12h7" stroke="var(--icon)" stroke-width="1.6"/></g>
      <g id="icon-gift" fill="#fff"><rect x="3" y="8" width="18" height="4"/><rect x="5" y="12" width="14" height="9"/><rect x="11" y="8" width="2" height="13" fill="var(--icon)"/><path d="M12 8c-2-4-6-4-6-1s6 1 6 1zM12 8c2-4 6-4 6-1s-6 1-6 1z"/></g>
    </defs>
  </svg>

  <section class="panel panel--talent">
    <h2 class="panel__title">Talent</h2>
    <p class="panel__intro">Lorem ipsum dolor sit amet, consectetur adipiscing elit. Pellentesque pulvinar urna orci, tempor vestibulum mi congue eget. Duis id odio non justo condimentum aliquet. Sed vitae metus id dui rutrum placerat eu sit amet enim. Nunc et lorem tincidunt, egestas ante ac, dignissim orci. Morbi sit amet justo tincidunt, gravida tellus malesuada, tincidunt dui. Curabitur suscipit pulvinar sem. Nulla fringilla dui vitae sagittis luctus. Sed cursus cursus dapibus. Duis vitae diam id ante rhoncus facilisis eu non quam. Nam fringilla, felis non sodales faucibus, nulla odio sollicitudin velit, vel condimentum neque justo eget magna. Morbi ipsum ligula, malesuada non neque non, vulputate porttitor ante. Duis eu turpis sapien.</p>
    <div class="features">
      <div class="feature c1 r1"><span class="feature__icon"><svg width="24" height="24"><use href="#icon-sun"/></svg></span><div><h3 class="feature__title">Online Resume</h3><p class="feature__text">Build your own resume with a direct link and share it with your network in the industry</p></div></div>
      <div class="feature c2 r1"><span class="feature__icon"><svg width="24" height="24"><use href="#icon-basket"/></svg></span><div><h3 class="feature__title">Head Shots</h3><p class="feature__text">Upload your professional head shots for casting directors and get noticed</p></div></div>
      <div class="feature c1 r2"><span class="feature__icon"><svg width="24" height="24"><use href="#icon-chat"/></svg></span><div><h3 class="feature__title">Audio Reel</h3><p class="feature__text">Upload your audio reel and showcase your voice over or singing skills</p></div></div>
      <div class="feature c2 r2"><span class="feature__icon"><svg width="24" height="24"><use href="#icon-gift"/></svg></span><div><h3 class="feature__title">Video Reel</h3><p class="feature__text">Link your demo reel directly from ReelStream and showcase your talent to casting directors</p></div></div>
      <div class="feature c1 r3"><span class="feature__icon"><svg width="24" height="24"><use href="#icon-basket"/></svg></span><div><h3 class="feature__title">Workshops</h3><p class="feature__text">Signup to our exclusive Acting and Performing workshops with industry professionals from Hollywood</p></div></div>
      <div class="feature c2 r3"><span class="feature__icon"><svg width="24" height="24"><use href="#icon-sun"/></svg></span><div><h3 class="feature__title">Casting Calls</h3><p class="feature__text">Search and submit our resume to the many listed auditions available locally and regionally through our network</p></div></div>
    </div>
  </section>

  <section class="panel panel--crew">
    <h2 class="panel__title">Crew</h2>
    <p class="panel__intro">Lorem ipsum dolor sit amet, consectetur adipiscing elit. Pellentesque pulvinar urna orci, tempor vestibulum mi congue eget. Duis id odio non justo condimentum aliquet. Sed vitae metus id dui rutrum placerat eu sit amet enim. Nunc et lorem tincidunt, egestas ante ac, dignissim orci. Morbi sit amet justo tincidunt, gravida tellus malesuada, tincidunt dui. Curabitur suscipit pulvinar sem. Nulla fringilla dui vitae sagittis luctus. Sed cursus cursus dapibus. Duis vitae diam id ante rhoncus facilisis eu non quam. Nam fringilla, felis non sodales faucibus, nulla odio sollicitudin velit, vel condimentum neque justo eget magna. Morbi ipsum ligula, malesuada non neque non, vulputate porttitor ante. Duis eu turpis sapien.</p>
    <div class="features">
      <div class="feature c1 r1"><span class="feature__icon"><svg width="24" height="24"><use href="#icon-sun"/></svg></span><div><h3 class="feature__title">Online Resume</h3><p class="feature__text">Build your own resume with a direct link and share it with your network in the industry</p></div></div>
      <div class="feature c2 r1"><span class="feature__icon"><svg width="24" height="24"><use href="#icon-basket"/></svg></span><div><h3 class="feature__title">Head Shots</h3><p class="feature__text">Upload your professional head shots for casting directors and get noticed</p></div></div>
      <div class="feature c1 r2"><span class="feature__icon"><svg width="24" height="24"><use href="#icon-chat"/></svg></span><div><h3 class="feature__title">Audio Reel</h3><p class="feature__text">Upload your audio reel and showcase your voice over or singing skills</p></div></div>
      <div class="feature c2 r2"><span class="feature__icon"><svg width="24" height="24"><use href="#icon-gift"/></svg></span><div><h3 class="feature__title">Video Reel</h3><p class="feature__text">Link your demo reel directly from ReelStream and showcase your talent to casting directors</p></div></div>
      <div class="feature c1 r3"><span class="feature__icon"><svg width="24" height="24"><use href="#icon-basket"/></svg></span><div><h3 class="feature__title">Workshops</h3><p class="feature__text">Signup to our exclusive Acting and Performing workshops with industry professionals from Hollywood</p></div></div>
      <div class="feature c2 r3"><span class="feature__icon"><svg width="24" height="24"><use href="#icon-sun"/></svg></span><div><h3 class="feature__title">Casting Calls</h3><p class="feature__text">Search and submit our resume to the many listed auditions available locally and regionally through our network</p></div></div>
    </div>
  </section>
</div>
</body>
</html>
```